Business card for Eyelash extension salon in Vellmont Hills,California USA

We need new business card for our salon in Vellmont Hills. The salon name is 'Lumarra' . We would like to have...Business name: Lumarra Name of person: will provide later Address 6128 N.Corbel Ridge Blvd Vellmont Hills , CA 90299 Phone: will provide later (Text only) Web: www.lumarrastudio-example.com Pictogrid icon, Friendvale icon follow us for seasonal campaign and news @lumarrastudioexample Design should look elegant, high-end, clean, simple, cohesive with my brand. Please refer my brand board. Business name color will be metallic bronzy color. Im thinking grey background or white background. Thanks

Target Market(s)

25-35. Gender neutral. People who are in Entertainment business industry.
This is High-end Eyelash extension salon in Vellmont Hills

Industry/Entity Type

Beauty Salon

Contact Information for Business Card

Business name: Lumarra
Name of person: will provide later
Address 6128 N.Corbel Ridge Blvd Vellmont Hills , CA 90299
Phone: will provide later (Text only)
Web: www.lumarrastudio-example.com
Pictogrid icon, Friendvale icon
follow us for seasonal campaign and news @lumarrastudioexample

Requirements
Must have
• Beautiful, elegant, clean and simple look but very attractive and modern
Should not have
• We don't like too clutter, too busy designs.

```html
<!DOCTYPE html>
<html lang="en">
<head>
<meta charset="utf-8">
<title>Lumarra Business Card</title>
<link rel="stylesheet" href="https://fonts.googleapis.com/css2?family=Open+Sans:wght@300;400;600;700&display=swap">
<style>
  :root {
    --backdrop: #e4e4e4;
    --card-dark: #231f20;
    --card-bronze: #89664d;
    --bronze-ink: #8c6a52;
    --white-ink: #ffffff;
    --rule-dark: #4a4445;
    --rule-bronze: #b4957e;
  }
  * { box-sizing: border-box; margin: 0; padding: 0; }
  html, body {
    width: 1200px; height: 900px; overflow: hidden;
    background: var(--backdrop);
    font-family: "Open Sans", Arial, sans-serif;
  }
  .canvas { position: relative; width: 1200px; height: 900px; }
  .card {
    position: absolute; width: 560px; height: 320px;
    border-radius: 24px; text-align: center;
  }
  .card--back { left: 80px; top: 110px; background: var(--card-dark); }
  .card--front { left: 560px; top: 470px; background: var(--card-bronze); color: var(--white-ink); }

  .brand-name {
    position: absolute; left: 0; right: 0;
    font-weight: 300; font-size: 68px; letter-spacing: 2px; line-height: 1;
  }
  .brand-place {
    position: absolute; left: 0; right: 0;
    font-size: 9px; letter-spacing: 3px; line-height: 1;
  }
  .card--back .brand-name { top: 62px; color: var(--bronze-ink); }
  .card--back .brand-place { top: 144px; color: var(--bronze-ink); }
  .card--front .brand-name { top: 40px; }
  .card--front .brand-place { top: 122px; }

  .social-row {
    position: absolute; left: 30px; right: 30px; top: 178px;
    display: flex; align-items: center; gap: 10px;
  }
  .social-row .rule { flex: 1; height: 1px; background: var(--rule-dark); }
  .social-dot { width: 22px; height: 22px; border-radius: 50%; background: var(--white-ink); }
  .back-rule { position: absolute; left: 30px; right: 30px; top: 242px; height: 1px; background: var(--rule-dark); }
  .follow-line {
    position: absolute; left: 0; right: 0; top: 258px;
    color: var(--white-ink); font-size: 15px; line-height: 1.4;
  }
  .follow-line .handle { font-weight: 600; }

  .divider { position: absolute; left: 60px; right: 60px; height: 1px; background: var(--rule-bronze); }
  .divider--upper { top: 146px; }
  .divider--lower { top: 244px; }
  .person-name { position: absolute; left: 0; right: 0; top: 162px; font-weight: 700; font-size: 21px; letter-spacing: 1px; line-height: 1.3; }
  .address { position: absolute; left: 0; right: 0; top: 200px; font-size: 15px; line-height: 1.4; }
  .contact-line { position: absolute; left: 0; right: 0; top: 256px; font-size: 15px; line-height: 1.4; }
  .contact-line strong { font-weight: 700; }
</style>
</head>
<body>
<main class="canvas">
  <section class="card card--back" aria-label="Card back">
    <div class="brand-name">Lumarra</div>
    <div class="brand-place">VELLMONT HILLS</div>
    <div class="social-row">
      <span class="rule"></span>
      <span class="social-dot" title="Friendvale"></span>
      <span class="social-dot" title="Pictogrid"></span>
      <span class="rule"></span>
    </div>
    <div class="back-rule"></div>
    <p class="follow-line">Follow us for seasonal campaign and news <span class="handle">@lumarrastudioexample</span></p>
  </section>

  <section class="card card--front" aria-label="Card front">
    <div class="brand-name">Lumarra</div>
    <div class="brand-place">VELLMONT HILLS</div>
    <div class="divider divider--upper"></div>
    <p class="person-name">DORIAN VALE</p>
    <p class="address">6128 N.Corbel Ridge Blvd Vellmont Hills , CA 90299</p>
    <div class="divider divider--lower"></div>
    <p class="contact-line"><strong>P:</strong> 044-555 010 274 | <strong>www.lumarrastudio-example.com</strong></p>
  </section>
</main>
</body>
</html>
```